Book Cover - The Velvet Lantern Almanac Collection

We are writing a book about the velvet lantern almanac collection, including Guerrilla Marketing. Advertising, Branding and PR.

We are looking for a fun and quirky cover, and are open to your ideas 💡
My website and social media are on www.TorvanPelica.co and posts are shared on Trelvano. Again we are open to ideas

```html
<!DOCTYPE html>
<html lang="en">
<head>
<meta charset="utf-8">
<title>The Velvet Lantern Almanac Collection – Book Cover</title>
<link rel="stylesheet" href="https://fonts.googleapis.com/css2?family=Alfa+Slab+One&family=Montserrat:wght@700;800&family=Zilla+Slab:wght@300&display=swap">
<style>
  :root {
    --page: #ffffff;
    --cover: #f8cda2;
    --orange: #ff7f1f;
    --orange-soft: #fba766;
    --photo-light: #e9e9ec;
    --photo-dark: #3c4150;
    --white: #ffffff;
    --shadow: #3a2a1e;
  }
  html, body {
    margin: 0;
    padding: 0;
    width: 1200px;
    height: 1200px;
    overflow: hidden;
    background: var(--page);
  }
  .canvas {
    position: relative;
    width: 1200px;
    height: 1200px;
  }
  .cover-spread {
    position: absolute;
    left: 241px;
    top: 340px;
    width: 717px;
    height: 521px;
    filter: drop-shadow(0 3px 4px rgba(0,0,0,0.25));
  }
  .back-title {
    font-family: "Montserrat", sans-serif;
    font-weight: 800;
    font-size: 24px;
    fill: var(--orange);
  }
  .author-bio {
    font-family: "Montserrat", sans-serif;
    font-weight: 700;
    font-size: 13.5px;
    fill: var(--orange);
  }
  .spine-title {
    font-family: "Montserrat", sans-serif;
    font-weight: 800;
    font-size: 20px;
    fill: var(--orange);
  }
  .sign-light {
    font-family: "Zilla Slab", serif;
    font-weight: 300;
    fill: var(--white);
  }
  .sign-bold {
    font-family: "Alfa Slab One", serif;
    fill: var(--white);
  }
  .sign-text {
    filter: drop-shadow(2px 2px 0 var(--shadow));
  }
</style>
</head>
<body>
<main class="canvas">
  <svg class="cover-spread" viewBox="0 0 1147 834" xmlns="http://www.w3.org/2000/svg" aria-label="Book cover: The Velvet Lantern Almanac Collection">
    <defs>
      <linearGradient id="billboard-tone" x1="0" y1="0" x2="0" y2="1">
        <stop offset="0" stop-color="var(--orange)"/>
        <stop offset="0.55" stop-color="var(--orange)"/>
        <stop offset="1" stop-color="var(--orange-soft)"/>
      </linearGradient>
      <linearGradient id="photo-tone" x1="0" y1="0" x2="0" y2="1">
        <stop offset="0" stop-color="var(--photo-light)"/>
        <stop offset="1" stop-color="var(--photo-dark)"/>
      </linearGradient>
    </defs>

    <rect class="cover-base" x="0" y="0" width="1147" height="834" fill="var(--cover)"/>

    <!-- Back cover -->
    <g class="back-cover">
      <text class="back-title" x="73" y="132">THE VELVET LANTERN</text>
      <text class="back-title" x="73" y="160">ALMANAC COLLECTION</text>
      <rect class="author-photo" x="73" y="191" width="140" height="140" fill="url(#photo-tone)" role="img" aria-label="Author portrait photograph"/>
      <text class="author-bio" x="233" y="201">I am Corin a Marketing student</text>
      <text class="author-bio" x="233" y="217">from Wexmoor, UK. I am currently</text>
      <text class="author-bio" x="233" y="233">studying level 3 extended diploma</text>
      <text class="author-bio" x="233" y="249">in marketing.</text>
      <rect class="barcode-area" x="349" y="692" width="180" height="108" fill="var(--white)"/>
    </g>

    <!-- Spine -->
    <text class="spine-title" transform="translate(567 208) rotate(90)" x="0" y="0" textLength="422" lengthAdjust="spacingAndGlyphs">THE VELVET LANTERN ALMANAC COLLECTION</text>

    <!-- Front cover -->
    <g class="front-cover">
      <rect class="billboard-artwork" x="637" y="90" width="459" height="744" fill="url(#billboard-tone)" role="img" aria-label="Billboard illustration on a tall pole carrying the book title"/>
      <g class="sign-text" text-anchor="middle">
        <text class="sign-light" x="866" y="208" font-size="62">THE</text>
        <text class="sign-bold" x="866" y="279" font-size="48" textLength="360" lengthAdjust="spacingAndGlyphs">VELVET LANTERN</text>
        <text class="sign-light" x="866" y="352" font-size="62" textLength="360" lengthAdjust="spacingAndGlyphs">ALMANAC</text>
        <text class="sign-bold" x="866" y="425" font-size="50" textLength="360" lengthAdjust="spacingAndGlyphs">COLLECTION</text>
      </g>
    </g>
  </svg>
</main>
</body>
</html>
```